New design for a physiotherapy clinic specializing in laser therapy

BrightPath Physiotherapy is a unique clinic specializing in laser therapy. The clinic is now 7 years old and has a well established reputation for patient care.

We are the largest laser physiotherapy clinic in Mississauga, ON, Canada. We use state of the art laser therapy equipment. Our knowledge base of how to use Low Level Laser Therapy in conjunction with traditional physiotherapy is what sets us apart. Nobody wants to live with pain and everyone wants to get better as quickly as possible. Our treatment methodology helps our patients return to normal lives quickly.

We want a website that communicates expertise, trust and shows that we care for our patients. We also want people to understand that the treatments are painless and speed up healing naturally.
Updates

Please include a location tab in your submission.  This page should have a map of our location and our phone number.

I do not want any white coat and stethoscope people. We do not see hospitalized patients. We use Vara-Kor NuvoTel laser web site www.nuvotelbeam.example please remove any images with other laser machines. I do not want "massage" therapy pictures as the main image. We treat post op total hip and knee replacements, rotator cuff injuries, osteoarthritic back pain patients, sprained ankles, degenerative disc disease problems as some of the more general injuries seen.

Industry/Entity Type

Clinic

Requirements
Must have
• We want to retain as much of the current content as possible. We will be looking at editing the content to make it shorter.

In addition to the current pages we want to add a blog page and link.

see our current site www.brightpathphysio.example
Nice to have
• Medical Images in the Whiplash and Auto Injuries should be re-drawn.

We want a clean, uncluttered look to the site.

Should not have
• Do not use illustrations of lasers shooting out or cutting. This is a "Cold" laser and does not cut. The laser procedure is gentle and soothing.

```html
<!DOCTYPE html>
<html lang="en">
<head>
<meta charset="utf-8">
<title>BrightPath Physiotherapy</title>
<link rel="stylesheet" href="https://fonts.googleapis.com/css2?family=Arimo:wght@400;700&family=Open+Sans:wght@600;700&display=swap">
<style>
:root{
  --green:#8cb43f;
  --green-light:#9cc24f;
  --white:#ffffff;
  --ink:#111111;
  --text:#666666;
  --rule:#e2e2e2;
  --footer:#f2f2f2;
  --dot:#3a3a3a;
}
*{margin:0;padding:0;box-sizing:border-box}
html,body{width:1010px;height:1200px;overflow:hidden;background:var(--white)}
body{position:relative;font-family:"Arimo",Arial,sans-serif;color:var(--text)}
.abs{position:absolute}
a{color:inherit}

.hero{left:0;top:0;width:1010px;height:417px;
  background:linear-gradient(100deg,#3d4a5c 0%,#6a7280 30%,#a9a7a3 55%,#c8c6bf 75%,#9fa890 100%)}
.hero-title{left:120px;top:278px;width:470px;font-family:"Open Sans",Arial,sans-serif;font-weight:700;font-size:25px;line-height:30px;color:var(--white);text-transform:uppercase}
.hero-sub{left:121px;top:338px;width:440px;font-family:"Open Sans",Arial,sans-serif;font-weight:700;font-size:11.5px;line-height:15px;color:var(--white);text-transform:uppercase}
.dots{left:839px;top:399px;display:flex;gap:3px}
.dots span{width:9px;height:7px;background:var(--dot)}

.header{left:81px;top:20px;width:841px;height:68px;background:var(--green)}
.logo{left:81px;top:19px;width:183px;height:70px;background:var(--white);display:flex;align-items:center;justify-content:center;gap:6px}
.logo-mark{width:10px;height:10px;border-radius:50%;background:var(--green)}
.logo-name{font-family:"Arimo",Arial,sans-serif;font-size:12.5px;font-weight:400;color:#333}
.nav{left:350px;top:48px;display:flex;gap:0;font-size:10.4px;font-weight:700;color:var(--white);text-transform:uppercase}
.nav span{margin-right:22px}
.nav span.tight{margin-right:12px}
.dropdown{left:510px;top:77px;width:139px;height:78px;background:var(--white);font-size:10.4px;font-weight:700;color:var(--ink)}
.dropdown div{height:29px;line-height:29px;padding-left:18px;margin-top:6px}
.dropdown div+div{border-top:1px solid var(--rule);margin-top:0}

.service{top:425px;width:262px;height:108px;background:linear-gradient(160deg,var(--green-light),var(--green));color:var(--white);padding:14px 20px}
.service h2{font-family:"Open Sans",Arial,sans-serif;font-weight:700;font-size:15px;letter-spacing:.2px;margin-bottom:20px}
.service p{font-size:10.3px;line-height:14.5px}
.service a{text-decoration:underline}

.h-who{left:100px;top:550px;font-size:15px;font-weight:700;color:var(--ink)}
.who-photo{left:99px;top:584px;width:156px;height:108px;background:linear-gradient(135deg,#e6e4e0,#b9aa9a 50%,#5a4a3e)}
.who-text{left:271px;top:584px;width:440px;font-size:10.2px;line-height:16px}
.who-text .more{color:var(--ink)}
.divider{left:81px;top:710px;width:582px;height:1px;background:var(--rule)}
.h-approach{left:98px;top:726px;font-size:12px;font-weight:700;color:var(--ink);text-transform:uppercase}
.approach{left:99px;top:752px;width:620px;font-size:10.2px;line-height:16px}
.approach p{margin-bottom:16px}

.h-side{font-size:11px;font-weight:700;color:var(--ink);text-transform:uppercase}
.info{left:736px;top:586px;width:186px;list-style:none}
.info li{height:25.3px;line-height:24px;font-size:10px;font-weight:700;color:var(--ink);border-bottom:1px solid var(--rule);padding-left:2px}
.info li:last-child{border-bottom:none}
.info li::before{content:"»";margin-right:9px}
.map{left:734px;top:884px;width:166px;height:92px;background:radial-gradient(ellipse at 55% 45%,#d7dde2,#eef1f3 70%,var(--white))}
.find-text{left:760px;top:886px;font-size:10px;font-weight:700;line-height:12.5px;color:#666}

.footer{left:0;top:1010px;width:1010px;height:190px;background:var(--footer)}
.f-links{left:101px;top:1026px;font-size:10.2px}
.f-links .home{font-weight:700;color:var(--ink);margin-bottom:12px}
.f-links div{height:21px}
.f-address{right:109px;top:1036px;text-align:right;font-size:10px;line-height:16.8px;color:#333}
.f-address .head{font-weight:700;color:var(--ink)}
.f-address .big{font-size:12.5px;font-weight:700;color:var(--ink);line-height:17px}
.f-address .follow{margin-top:8px;color:var(--ink)}
.social{left:794px;top:1166px;display:flex;gap:2px}
.social span{width:27px;height:27px;border-radius:50%;border:2px solid #c9c9c9}
.social .s1{background:#e8682a}.social .s2{background:#c8372d}.social .s3{background:#3b5a9a}.social .s4{background:#36a4dc}
</style>
</head>
<body>

<div class="abs hero" role="img" aria-label="Photo of a young woman with a minor head injury sitting beside a damaged car after a collision"></div>
<div class="abs hero-title">More than 7 years of dedication and service</div>
<div class="abs hero-sub">BrightPath Physiotherapy is committed to helping you get better, faster, with fewer treatments.</div>
<div class="abs dots"><span></span><span></span><span></span><span></span><span></span></div>

<div class="abs header"></div>
<div class="abs logo"><span class="logo-mark"></span><span class="logo-name">BrightPath Physiotherapy</span></div>
<nav class="abs nav">
  <span>Home</span><span>Clinic Hours</span><span>Theraphy</span><span>Whiplash &amp; Auto Injuries</span><span>News</span><span class="tight">Location</span><span>Blog</span>
</nav>
<div class="abs dropdown"><div>Physiotheraphy</div><div>Massage Theraphy</div></div>

<section class="abs service" style="left:81px">
  <h2>PHYSIOTHERAPHY</h2>
  <p>Sed ut perspiciatis unde omnis iste natus error sit voluptatem accusantium doloremque lauda<br><a>Click here to know more</a></p>
</section>
<section class="abs service" style="left:375px;padding-top:10px">
  <h2>LASER THERAPHY</h2>
  <p>Sed ut perspiciatis unde omnis iste natus error sit voluptatem accusantium doloremque lauda<br><a>Click here to know more</a></p>
</section>
<section class="abs service" style="left:660px;padding-top:10px">
  <h2>MASSAGE THERAPHY</h2>
  <p>Sed ut perspiciatis unde omnis iste natus error sit voluptatem accusantium doloremque lauda<br><a>Click here to know more</a></p>
</section>

<h2 class="abs h-who">WHO WE ARE?</h2>
<div class="abs who-photo" role="img" aria-label="Photo of a smiling older man and a young woman seated together"></div>
<p class="abs who-text">We are Mississauga's premier physiotherapy and low intensity laser therapy specialists.&nbsp; We integrate low intensity laser therapy (laser therapy or cold laser therapy) with physiotherapy to safely and effectively treat a wide variety of musculoskeletal injuries and inflammatory conditions &nbsp;(i.e. back pain, arthritis, knee injuries, shoulder injuries, tendonitis, bursitis, repetitive strains, auto &amp; sports injuries).&nbsp; We Use a multi-faceted regime of clinically tested and proven protocols with one goal in mind: Get you better, faster.<br><span class="more">Read more..</span></p>
<div class="abs divider"></div>

<h2 class="abs h-approach">BrightPath's unique treatment approach</h2>
<div class="abs approach">
  <p>&nbsp;When we combine laser therapy with traditional physiotherapy mobilization and strengthening, the results are remarkable.<br>Low Intensity Laser Therapy (LILT), also know as biophotostimulation, helps restore normal cellular function while enhancing the body's natural healing processes.&nbsp; The laser treatments are painless.&nbsp; Frequently, patients will experience a reduction in pain after their first treatment and sleep more soundly that evening.</p>
  <p>At BrightPath, we use the NuvoTel Professional Laser Therapy System exclusively.&nbsp; The NuvoTel system was developed by a Canadian surgeon, Dr. Alan Merrow, and is the most sophisticated laser therapy system available.&nbsp; All treatments with the NuvoTel system uses three stages, each stage has a different wavelength of light and different dosage.&nbsp; This unique procedure produces a superior therapeutic effect.</p>
  <p>Laser therapy sessions range from 30 to 60 minutes depending on the condition treated. As you advance through the healing process with LILT, pain is substantially diminished.&nbsp; However, patients may require improvement in their range of motion, muscle balancing and strengthening in order to avoid re-injury.</p>
</div>

<h3 class="abs h-side" style="left:731px;top:553px">Information Desk</h3>
<ul class="abs info">
  <li>Home</li><li>Contact Information</li><li>Clinic Hours</li><li>Visting our clinic - FAQ</li><li>Insurance</li><li>Testimonials</li><li>Bright Path in the News</li><li>Patient Forms</li><li>Employement Opportunities</li><li>Whiplash &amp; Auto Injuries</li>
</ul>
<h3 class="abs h-side" style="left:734px;top:852px;font-size:12px">Find Us Here</h3>
<div class="abs map" role="img" aria-label="Faint world map"></div>
<div class="abs find-text">Westbrook Centre, 1480<br>Oakline Parkway,<br>Mississauga,<br>ON L5X 2R4<br>CALL: 905-555-0142</div>

<footer class="abs footer"></footer>
<div class="abs f-links">
  <div class="home">HOME</div>
  <div>Contact</div><div>Massage Theraphy</div><div>Laser Theraphy</div><div>Physiotheraphy</div><div>Whiplash &amp; Auto</div><div>Injuries</div>
</div>
<div class="abs f-address">
  <div class="head">OUR ADDRESS</div>
  <div>Westbrook Centre, 1480 Oakline Parkway, Mississauga, ON L5X 2R4</div>
  <div>One block north of the QEW on Oakline Parkway</div>
  <div>We are located in the lower level of the mall, by the library</div>
  <div class="big">Telephone: 905-555-0142</div>
  <div class="big">FAX: 905-555-0187</div>
  <div class="follow">Follow us on:</div>
</div>
<div class="abs social">
  <span class="s1" role="img" aria-label="Feed"></span>
  <span class="s2" role="img" aria-label="Social network"></span>
  <span class="s3" role="img" aria-label="Social network"></span>
  <span class="s4" role="img" aria-label="Social network"></span>
</div>

</body>
</html>
```